The Seven Gates CD cover and booklet - meditation walks

I have created a CD of five meditation walks for the modern mystic - with a professional voice over and really cool music - to help people find their way back home to their true Self. It is very powerful and life-enhancing. The walks were created on the Canary Island of Lanzarote in Mateo's garden and I have stunning photographs taken by pro-photographer Derek Holbrook to accompany the sleeve notes. The result will be a truly beautiful 12pp CD sleeve note booklet - which will itself be so cleanly laid out people will want to pick it up and play! :-) You can do that for me ... and, of course, you will get a free signed copy of the finished CD ... Gus - The Seven Gates - see http://www.quietharbor-retreat.com/
I will send a CD page layout template, the full text and hi-res images to the selected design partner. I attach sample text docs and lo-res logo.
Extra guaranteed money and extended deadline with helpful files.
Hi there - I'm very excited about what designs I get for The Seven Gates CD. Everything is ready to go!
Gus
Today I have uploaded a hi-res version of The Seven Gates logo which you may find helpful.
Gus
Several designers have requested hi-res images of the pictures on the PDF sample pages - so I have uploaded this evening some additional hi-res images as well as a hi-res logo.
hi all you lovely designers! Today is the last day for submission of designs - so if you want a shout ... its now or never. :-)
Photographer

```html
<!DOCTYPE html>
<html lang="en">
<head>
<meta charset="utf-8">
<title>The Seven Gates – CD cover and inlay</title>
<link rel="stylesheet" href="https://fonts.googleapis.com/css2?family=Mulish:ital,wght@0,300;0,400;1,300&display=swap">
<style>
  :root {
    --page: #ffffff;
    --navy: #1f3566;
    --navy-light: #4b5f92;
    --sea-deep: #2f7f95;
    --sea-foam: #c9d6d6;
    --sand: #b88a62;
    --sand-dark: #9a6e4c;
    --turquoise: #36bcc4;
    --turquoise-light: #4cc8ce;
    --spine: #6fd0d3;
    --white: #ffffff;
    --shadow: 3px 4px 7px rgba(0, 0, 0, 0.28);
  }
  * { box-sizing: border-box; margin: 0; padding: 0; }
  html, body { width: 1200px; height: 848px; overflow: hidden; background: var(--page); }
  body { position: relative; font-family: "Mulish", sans-serif; font-weight: 300; color: var(--white); }

  .panel { position: absolute; box-shadow: var(--shadow); overflow: hidden; }

  /* Front cover */
  .front-cover { left: 212px; top: 48px; width: 374px; height: 370px; }
  .front-cover .beach-photo {
    position: absolute; inset: 0;
    background: linear-gradient(180deg, var(--sea-deep) 0%, #5f9aa6 14%, var(--sea-foam) 26%, #c9a98a 40%, var(--sand) 60%, var(--sand-dark) 100%);
  }
  .title-band {
    position: absolute; left: 96px; top: 68px; width: 278px; height: 90px;
    background: var(--navy); border-top: 12px solid var(--navy-light);
    text-align: right; padding: 10px 12px 0 0;
  }
  .title-band h1 { font-weight: 300; font-size: 24px; line-height: 1.2; letter-spacing: 0.2px; }
  .title-band p { font-size: 12.5px; margin-top: 6px; }
  .credit-line { position: absolute; right: 68px; bottom: 19px; font-size: 10.5px; }
  .publisher-badge {
    position: absolute; right: 0; bottom: 0; width: 62px; height: 51px;
    background: var(--navy); display: flex; flex-direction: column;
    align-items: center; justify-content: center; gap: 4px;
    font-size: 8px; text-align: center;
  }
  .publisher-badge .mark { width: 12px; height: 12px; background: var(--white); }

  /* Back inlays */
  .back-cover { left: 615px; top: 48px; width: 374px; height: 370px; }
  .tray-inlay { left: 368px; top: 435px; width: 465px; height: 365px; }
  .water-photo {
    position: absolute; inset: 0;
    background: radial-gradient(ellipse at 60% 40%, var(--turquoise-light), var(--turquoise) 70%);
  }
  .spine {
    position: absolute; top: 0; bottom: 0; width: 18px; background: var(--spine);
    display: flex; align-items: center; justify-content: center;
  }
  .spine-left { left: 0; }
  .spine-right { right: 0; }
  .spine span { white-space: nowrap; font-size: 7px; transform-origin: center; }
  .spine-left span { transform: rotate(-90deg); }
  .spine-right span { transform: rotate(90deg); }

  .notes { position: absolute; font-size: 10px; }
  .back-cover .notes { left: 25px; top: 52px; width: 330px; }
  .tray-inlay .notes { left: 53px; top: 50px; width: 370px; font-size: 10.5px; }
  .notes h2 { font-weight: 300; font-size: 1.8em; line-height: 1.1; margin-bottom: 3px; }
  .track-list { list-style: none; width: 11.5em; font-size: 0.92em; line-height: 1.42; }
  .track-list li { display: flex; justify-content: space-between; }
  .quote { font-style: italic; font-size: 1.3em; margin-top: 1.1em; }
  .quote-source { font-size: 0.9em; margin-top: 0.2em; }
  .blurb { font-size: 0.82em; line-height: 1.3; margin-top: 1.6em; width: 36em; }
  .imprint { margin-top: 3.2em; display: flex; flex-direction: column; gap: 2px; font-size: 0.6em; }
  .imprint .publisher-name { display: flex; align-items: center; gap: 5px; font-size: 1.6em; margin-bottom: 2px; }
  .imprint .publisher-name i { width: 11px; height: 11px; background: var(--navy); display: inline-block; }
  .photo-credit { position: absolute; font-size: 6px; }
  .back-cover .photo-credit { left: 25px; bottom: 13px; }
  .tray-inlay .photo-credit { left: 53px; bottom: 15px; font-size: 6.3px; }
</style>
</head>
<body>

  <section class="panel front-cover">
    <div class="beach-photo" role="img" aria-label="Photograph of footprints in wet sand leading away from breaking waves on a beach"></div>
    <div class="title-band">
      <h1>the Seven Gates</h1>
      <p>walking meditations for the mystic in you</p>
    </div>
    <p class="credit-line">created by Gus Merriweather</p>
    <div class="publisher-badge"><span class="mark"></span>Lumen Press</div>
  </section>

  <section class="panel back-cover">
    <div class="water-photo" role="img" aria-label="Aerial photograph of clear turquoise water with dark rocks beneath the surface"></div>
    <div class="notes">
      <h2>the Seven Gates</h2>
      <ol class="track-list">
        <li><span>1. Introduction</span><span>3:52</span></li>
        <li><span>2. Via Positiva</span><span>9:04</span></li>
        <li><span>3. Via Negativa</span><span>6:54</span></li>
        <li><span>4. Via Creativa</span><span>6:22</span></li>
        <li><span>4. Via Transformativa</span><span>5:52</span></li>
        <li><span>5. Via Integrativa</span><span>4:53</span></li>
      </ol>
      <p class="quote">“What you are looking for is what is looking.”</p>
      <p class="quote-source">Brother Anselm</p>
      <p class="blurb">These walking meditations created in Mateo’s garden, Lanzarote will make you feel grounded and uplifted, centred and expansive, connected with your deepest purpose and your true Self.</p>
      <div class="imprint">
        <span class="publisher-name"><i></i>Lumen Press</span>
        <span>© Lumen Press 2013</span>
        <span>www.sevengatesaudio.com</span>
      </div>
    </div>
    <p class="photo-credit">photo: Playa de las Conchas, La Graciosa, Lanzarote, Canary Islands by Derek Holbrook, qr8</p>
  </section>

  <section class="panel tray-inlay">
    <div class="water-photo" role="img" aria-label="Aerial photograph of clear turquoise water with dark rocks beneath the surface"></div>
    <div class="spine spine-left"><span>the Seven Gates walking meditations for the mystic in you</span></div>
    <div class="spine spine-right"><span>the Seven Gates walking meditations for the mystic in you</span></div>
    <div class="notes">
      <h2>the Seven Gates</h2>
      <ol class="track-list">
        <li><span>1. Introduction</span><span>3:52</span></li>
        <li><span>2. Via Positiva</span><span>9:04</span></li>
        <li><span>3. Via Negativa</span><span>6:54</span></li>
        <li><span>4. Via Creativa</span><span>6:22</span></li>
        <li><span>4. Via Transformativa</span><span>5:52</span></li>
        <li><span>5. Via Integrativa</span><span>4:53</span></li>
      </ol>
      <p class="quote">“What you are looking for is what is looking.”</p>
      <p class="quote-source">Brother Anselm</p>
      <p class="blurb">These walking meditations created in Mateo’s garden, Lanzarote will make you feel grounded and uplifted, centred and expansive, connected with your deepest purpose and your true Self.</p>
      <div class="imprint">
        <span class="publisher-name"><i></i>Lumen Press</span>
        <span>© Lumen Press 2013</span>
        <span>www.sevengatesaudio.com</span>
      </div>
    </div>
    <p class="photo-credit">photo: Playa de las Conchas, La Graciosa, Lanzarote, Canary Islands by Derek Holbrook, qr8</p>
  </section>

</body>
</html>
```